Kindro - Bringing Warmth and Quality to Senior Living

We are a new company based in Sydney, Australia. We have developed a state-of-the-art app for communication between aged care facilities and families.

Kindro has been developed for facilities to augment the best possible care by providing easy, safe and secure communication for families to stay in touch with their loved ones.
Updates

the website needs to be designed so we can add functionality including multilingual support. display in different languages.we also require enquiry and email/data base function. we want it simple and clean so its responsive. the target audience will be 40+ in age. there will be a video on home page. would like to start with 6 pages/ subjects -homepage -about us -our solution -demonstration page, this will be a page that contains videos of people using our product -customer testimonials -contact us

Target Market(s)

Aged care facilities.
Families (over 40’s age group) who are looking for a facility for their loved ones.

Number of Pages Required

5+ page

Font styles to use
Sans Serif

Colors
faa54b
ffffff
0255a3

Requirements
Must have
• - Our corporate colour is #EE8811.
• - If you're using stock photography, please use brimlo prints photos as we have a license for their photos.
• - The design needs to be responsive (mobile and desktop)
• -White space on each page
Nice to have
• -need to leave a place for a future animation video to be added in on the home tab
Should not have
• we don't want flash technology

```html
<!DOCTYPE html>
<html lang="en">
<head>
<meta charset="utf-8">
<title>Kindro - Bringing Warmth and Quality to Senior Living</title>
<link rel="stylesheet" href="https://fonts.googleapis.com/css2?family=Ubuntu:wght@400;500;700&family=Open+Sans:ital,wght@0,400;0,600;0,700;1,400&display=swap">
<style>
:root{
  --orange:#f7931e;
  --orange-soft:#faa54b;
  --blue:#0255a3;
  --peach:#fde6cf;
  --ink:#2b2b2b;
  --text:#444;
  --muted:#666;
  --pale:#f5f7fc;
  --white:#fff;
  --teal:#3dbb96;
}
*{margin:0;padding:0;box-sizing:border-box}
html,body{width:1200px;height:3084px;overflow:hidden}
body{position:relative;background:var(--white);font-family:'Open Sans',sans-serif;color:var(--text)}
.abs{position:absolute}
.brand{font-family:'Ubuntu',sans-serif;font-weight:500;font-size:31px;color:var(--orange);display:flex;align-items:center;gap:8px}
.brand-dot{width:26px;height:26px;border:3px solid var(--orange);border-radius:50%}
.nav{top:34px;left:612px;display:flex;gap:26px;font-size:11px;font-weight:600;color:#333;letter-spacing:.2px}
.nav .active{color:var(--orange)}
.hero-bg{left:0;top:0;width:1200px;height:520px;overflow:hidden}
.hero-title{left:238px;top:138px;font-family:'Ubuntu',sans-serif;font-weight:700;font-size:43px;line-height:46px;color:var(--ink)}
.hero-copy{left:240px;top:246px;width:340px;font-size:10.5px;line-height:16px;color:#333}
.hero-copy .name{color:var(--orange)}
.btn{left:240px;top:320px;width:113px;height:34px;background:var(--orange);color:#fff;font-size:10px;font-weight:700;display:flex;align-items:center;justify-content:center;box-shadow:0 8px 16px rgba(247,147,30,.35)}
.phone{left:790px;top:86px;width:190px;height:364px;background:#111;border-radius:12px;border:3px solid #ddd;box-shadow:0 4px 10px rgba(0,0,0,.25)}
.phone-screen{position:absolute;left:8px;top:18px;right:8px;bottom:18px;background:linear-gradient(#fff 0 40%,#8a3a30 40% 72%,#e4a08e 72% 100%)}
.about{left:198px;top:599px;width:762px;height:363px;box-shadow:0 4px 18px rgba(0,0,0,.08);background:#fff}
.video{position:absolute;left:0;top:0;width:448px;height:363px;background:var(--blue)}
.play{position:absolute;left:174px;top:120px;width:100px;height:100px;border-radius:50%;background:rgba(255,255,255,.25)}
.play::before{content:"";position:absolute;left:12px;top:12px;width:76px;height:76px;border-radius:50%;background:rgba(255,255,255,.35)}
.play::after{content:"";position:absolute;left:21px;top:21px;width:58px;height:58px;border-radius:50%;background:#fff}
.play svg{position:absolute;left:40px;top:38px;z-index:2}
.video-label{position:absolute;left:0;width:448px;top:238px;text-align:center;color:#fff;font-size:9.5px;font-weight:700}
.about-text{position:absolute;left:474px;top:30px;width:264px}
.eyebrow{font-size:9.5px;font-weight:700;color:var(--orange);letter-spacing:.3px}
.about-text h2{font-family:'Ubuntu',sans-serif;font-weight:400;font-size:22px;color:var(--ink);margin-top:8px}
.rule{width:24px;height:2px;background:var(--orange);margin:8px 0 12px}
.about-text p{font-size:9.5px;line-height:15px;color:#444}
.section-head{left:0;width:1200px;text-align:center}
.section-head h2{font-family:'Ubuntu',sans-serif;font-weight:400;font-size:32px;color:var(--ink);margin-top:4px}
.section-head .rule{margin:8px auto 0}
.card{background:#fff;box-shadow:0 3px 14px rgba(0,0,0,.09)}
.feature{width:175px;height:175px;display:flex;flex-direction:column;align-items:center;justify-content:center;text-align:center;font-size:10px;line-height:15px;color:#333;padding:0 12px}
.feature svg{margin-bottom:14px}
.benefit{width:353px;height:276px;padding:24px 18px}
.b-item{display:flex;gap:16px}
.b-item h3{font-family:'Ubuntu',sans-serif;font-weight:500;font-size:16px;color:var(--ink);margin:20px 0 12px}
.b-item ul{list-style:none}
.b-item li{font-size:9.5px;line-height:14px;margin-bottom:8px;position:relative;padding-left:14px;color:#333}
.b-item li::before{content:"";position:absolute;left:0;top:4px;width:6px;height:6px;border-radius:50%;background:var(--orange)}
.icon{width:40px;flex:none;margin-top:10px}
.quote{padding:22px 24px;font-size:9.5px;line-height:16px;font-style:italic;color:#333;border:1px solid #eee}
.quote.main{border:none;box-shadow:0 4px 16px rgba(0,0,0,.1)}
.arrow{width:36px;height:36px;border-radius:50%;background:var(--orange);box-shadow:0 0 0 5px #fde2c4;display:flex;align-items:center;justify-content:center}
.person{display:flex;align-items:center;gap:16px;font-size:11px;font-weight:700;color:#222}
.avatar{width:38px;height:38px;border-radius:50%;background:linear-gradient(135deg,#5a6470,#2f3540)}
.team{width:113px;text-align:center}
.photo{width:113px;height:112px}
.team h4{font-size:12px;font-weight:700;color:#222;margin-top:12px;white-space:nowrap}
.team p{font-size:10px;color:#333;margin-top:3px;white-space:nowrap}
.footer{left:0;top:2835px;width:1200px;height:249px;background:var(--blue);color:#fff}
.footer .brand{color:#fff;position:absolute;left:88px;top:38px}
.footer .brand-dot{border-color:#fff}
.f-about{position:absolute;left:88px;top:96px;width:160px;font-size:8.5px;line-height:16px}
.f-copy{position:absolute;left:88px;top:184px;font-size:8.5px;font-weight:600}
.f-nav{position:absolute;left:387px;top:42px;list-style:none;font-size:9px;font-weight:700}
.f-nav li{margin-bottom:12px}
.f-contact{position:absolute;left:590px;top:42px;font-size:9px}
.f-contact h5{font-size:9px;font-weight:700;display:flex;gap:6px;align-items:center}
.f-contact p{margin:10px 0 0 16px}
.f-social{position:absolute;left:886px;top:42px;font-size:9px;font-weight:700}
.f-social .row{display:flex;gap:10px;margin-top:14px}
.f-social .row span{width:24px;height:24px;border-radius:50%;background:#fff;opacity:.9}
</style>
</head>
<body>

<div class="abs hero-bg">
  <svg width="1200" height="520" aria-hidden="true">
    <circle cx="1020" cy="210" r="440" fill="var(--peach)"/>
    <circle cx="886" cy="270" r="188" fill="var(--blue)"/>
  </svg>
</div>

<div class="abs brand" style="left:88px;top:20px"><span class="brand-dot"></span>Kindro</div>
<nav class="abs nav">
  <span class="active">HOME</span><span>ABOUT US</span><span>OUR SOLUTION</span><span>DEMONSTRATION</span><span>TESTIMONIALS</span><span>CONTACT US</span>
</nav>

<h1 class="abs hero-title">Frequent contact<br>with loved ones.</h1>
<p class="abs hero-copy"><span class="name">Kindro</span> has been developed for facilities to augment the best possible care by providing easy, safe and secure communication for families to stay in touch with their loved ones.</p>
<div class="abs btn">LEARN MORE</div>

<div class="abs phone">
  <div class="phone-screen" role="img" aria-label="App screen showing a resident meal report with a photo of a plated meal"></div>
</div>

<section class="abs about">
  <div class="video">
    <div class="play"><svg width="22" height="24"><path d="M0 0L20 12L0 24Z" fill="var(--orange)"/></svg></div>
    <div class="video-label">Watch The Video</div>
  </div>
  <div class="about-text">
    <div class="eyebrow">ABOUT US</div>
    <h2>Who are We ?</h2>
    <div class="rule"></div>
    <p>We are a Sydney based, family owned business who have combined experiences from many walks of life that have led us to produce a solution for an issue that was of great concern to us. &nbsp;Our backgrounds encompass 40 years of software development, decades of experience in marketing management and service delivery and over 10 years within the childcare industry.</p>
    <h2 style="margin-top:20px">The Origin of Kindro</h2>
    <div class="rule"></div>
    <p>The founders were concerned by the lack of communication during their loved ones' time in residential aged care.With demands on staff resources it was difficult to speak with the right person at the right time.With,this in mind, Kindro was developed to improve quality and accountability of care.</p>
  </div>
</section>

<svg class="abs" style="left:0;top:1220px" width="1200" height="845" aria-hidden="true">
  <path d="M0 140 Q600 -130 1200 140 L1200 845 L0 845 Z" fill="var(--pale)"/>
</svg>

<div class="abs section-head" style="top:1064px">
  <div class="eyebrow">OUR SOLUTION</div>
  <h2>Kindro Feature</h2>
  <div class="rule"></div>
</div>

<div class="abs card feature" style="left:313px;top:1157px">
  <svg width="60" height="56" aria-hidden="true"><rect x="2" y="6" width="36" height="48" rx="4" fill="var(--teal)"/><rect x="6" y="12" width="28" height="34" fill="#fff"/><rect x="40" y="18" width="18" height="36" rx="3" fill="var(--teal)"/><rect x="43" y="23" width="12" height="24" fill="#fff"/><circle cx="20" cy="50" r="2" fill="#fff"/></svg>
  Works on phones and tablet devices.
</div>
<div class="abs card feature" style="left:513px;top:1157px">
  <svg width="60" height="60" aria-hidden="true"><rect x="6" y="4" width="28" height="50" rx="4" fill="#fff" stroke="#222" stroke-width="2"/><rect x="10" y="10" width="20" height="36" fill="#bfe3f3"/><path d="M26 32q10-6 20 4q8 10 0 20q-10 4-20-6Z" fill="#f6c08f" stroke="#222" stroke-width="2"/></svg>
  Simple to use.
</div>
<div class="abs card feature" style="left:713px;top:1157px">
  <svg width="54" height="64" aria-hidden="true"><rect x="2" y="4" width="50" height="58" fill="#e9573f"/><rect x="9" y="12" width="36" height="44" fill="#fff"/><rect x="18" y="0" width="18" height="10" fill="#ccc"/><g fill="#333"><rect x="15" y="22" width="24" height="3"/><rect x="15" y="30" width="24" height="3"/><rect x="15" y="38" width="24" height="3"/><rect x="15" y="46" width="16" height="3"/></g></svg>
  Provides frequent resident updates to families such as meal reports, activities...
</div>
<div class="abs card feature" style="left:412px;top:1357px">
  <svg width="64" height="60" aria-hidden="true"><rect x="2" y="4" width="60" height="40" rx="3" fill="#f5c542" stroke="#333" stroke-width="2"/><circle cx="32" cy="22" r="12" fill="#e9573f" stroke="#333" stroke-width="2"/><rect x="26" y="44" width="12" height="8" fill="#5bb0d9"/><rect x="18" y="52" width="28" height="4" fill="#333"/></svg>
  Residents privacy is ensured by the use of advanced artificial intelligence processes.
</div>
<div class="abs card feature" style="left:612px;top:1357px">
  <svg width="64" height="62" aria-hidden="true"><path d="M32 2L54 10V28Q54 44 32 52Q10 44 10 28V10Z" fill="#f5c542" stroke="#333" stroke-width="2"/><path d="M22 26l7 7 13-13" fill="none" stroke="#333" stroke-width="3"/><rect x="4" y="42" width="56" height="18" fill="#e8a864" stroke="#333" stroke-width="2"/></svg>
  Kindro complies with the requir-ements of Privacy Act 1988 (Cth) Information is protected
</div>

<div class="abs section-head" style="top:1618px">
  <div class="eyebrow">BENEFITS</div>
  <h2>Kindro Benefit</h2>
  <div class="rule"></div>
</div>

<div class="abs card benefit" style="left:238px;top:1712px">
  <div class="b-item">
    <svg class="icon" width="40" height="40" aria-hidden="true"><rect x="4" y="8" width="32" height="30" fill="#dfe6ee" stroke="#333" stroke-width="2"/><rect x="14" y="2" width="12" height="8" fill="#e9573f"/><g fill="#5b8fd9"><rect x="9" y="14" width="6" height="6"/><rect x="25" y="14" width="6" height="6"/><rect x="9" y="24" width="6" height="6"/><rect x="25" y="24" width="6" height="6"/></g><rect x="17" y="28" width="6" height="10" fill="#e9573f"/></svg>
    <div><h3>Facilities</h3><ul><li>Offers families proof of excellent care.</li><li>Competitive advantages over other facilities.</li><li>Very little additional work for carers and management</li><li>Allows carers to demonstrate the quality of their work.</li></ul></div>
  </div>
  <div class="b-item" style="margin-top:2px">
    <svg class="icon" width="40" height="36" aria-hidden="true"><path d="M2 18L20 4L38 18V34H2Z" fill="#f5c542" stroke="#333" stroke-width="2"/><rect x="15" y="22" width="10" height="12" fill="#8a5a3b"/></svg>
    <div><h3>Residents</h3><ul><li>Easier communication between residents and families.</li></ul></div>
  </div>
</div>

<div class="abs card benefit" style="left:610px;top:1712px">
  <div class="b-item">
    <svg class="icon" width="40" height="40" aria-hidden="true"><g fill="#8fa7bf" stroke="#333" stroke-width="1.5"><rect x="3" y="16" width="10" height="22"/><rect x="15" y="14" width="10" height="24"/><rect x="27" y="18" width="10" height="20"/><circle cx="8" cy="10" r="5"/><circle cx="20" cy="8" r="5"/><circle cx="32" cy="12" r="5"/></g></svg>
    <div><h3>Families</h3><ul><li>Frequent contact with loved ones</li><li>Families will better informed and have more valuable interactions with facilities and staff.</li><li>Facility trust.</li></ul></div>
  </div>
  <div class="b-item" style="margin-top:8px">
    <svg class="icon" width="40" height="36" aria-hidden="true"><rect x="14" y="0" width="12" height="8" fill="none" stroke="#333" stroke-width="2"/><rect x="2" y="6" width="36" height="28" rx="3" fill="#e9573f"/><path d="M20 12v16M12 20h16" stroke="#fff" stroke-width="5"/></svg>
    <div><h3>Carers</h3><ul><li>Ability to access a simple method of quality care.</li></ul></div>
  </div>
</div>

<div class="abs section-head" style="top:2132px">
  <div class="eyebrow">TESTIMONIALS</div>
  <h2>What people are saying</h2>
  <div class="rule"></div>
</div>

<div class="abs arrow" style="left:198px;top:2282px"><svg width="8" height="10" aria-hidden="true"><path d="M8 0V10L0 5Z" fill="#fff"/></svg></div>
<div class="abs arrow" style="left:966px;top:2282px"><svg width="8" height="10" aria-hidden="true"><path d="M0 0V10L8 5Z" fill="#fff"/></svg></div>

<div class="abs card quote" style="left:247px;top:2244px;width:218px;height:113px">" Lorem ipsum dolor sit amet, consecte adipiscing elit, sed do eiusmod tempor incididunt ut labore et dolore magna ipsum suspendisse ultrices gravida. "</div>
<div class="abs card quote main" style="left:480px;top:2232px;width:239px;height:125px">" Lorem ipsum dolor sit amet, consecte adipiscing elit, sed do eiusmod tempor incididunt ut labore et dolore magna ipsum suspendisse ultrices gravida. "</div>
<svg class="abs" style="left:522px;top:2356px" width="20" height="10" aria-hidden="true"><path d="M0 0H20L10 10Z" fill="#fff"/></svg>
<div class="abs card quote" style="left:734px;top:2244px;width:219px;height:113px">" Lorem ipsum dolor sit amet, consecte adipiscing elit, sed do eiusmod tempor incididunt ut labore et dolore magna ipsum suspendisse ultrices gravida. "</div>

<div class="abs person" style="left:255px;top:2380px"><span class="avatar" role="img" aria-label="Reviewer portrait"></span>John Doe</div>
<div class="abs person" style="left:486px;top:2380px;color:var(--orange)"><span class="avatar" role="img" aria-label="Reviewer portrait"></span>John Doe</div>
<div class="abs person" style="left:745px;top:2380px"><span class="avatar" role="img" aria-label="Reviewer portrait"></span>John Doe</div>

<div class="abs section-head" style="top:2492px">
  <div class="eyebrow">STAFF</div>
  <h2>OUR TEAM</h2>
  <div class="rule"></div>
</div>

<div class="abs team" style="left:211px;top:2586px"><div class="photo" role="img" aria-label="Portrait of Owen Halloway" style="background:linear-gradient(#dfe3e8,#8aa3c4)"></div><h4>Owen Halloway</h4><p>Lead Developer</p></div>
<div class="abs team" style="left:342px;top:2586px"><div class="photo" role="img" aria-label="Portrait of Grant Ellery" style="background:linear-gradient(#e4e4e4,#555)"></div><h4>Grant Ellery</h4><p>A founder of Kindro</p></div>
<div class="abs team" style="left:473px;top:2586px"><div class="photo" role="img" aria-label="Portrait of Tessa Moreland" style="background:linear-gradient(#e6e6e6,#d9b77a)"></div><h4>Tessa Moreland</h4><p>Childcare Educator</p></div>
<div class="abs team" style="left:604px;top:2586px"><div class="photo" role="img" aria-label="Portrait of Nina Castell" style="background:linear-gradient(#eee,#c9a27a)"></div><h4>Nina Castell</h4></div>
<div class="abs team" style="left:735px;top:2586px"><div class="photo" role="img" aria-label="Portrait of Reid Carrow" style="background:linear-gradient(#2aa5b5,#1c2530)"></div><h4>Reid Carrow</h4></div>
<div class="abs team" style="left:872px;top:2586px"><div class="photo" role="img" aria-label="Portrait of Lucy Ann Penfold" style="background:linear-gradient(#e9e9e9,#b9764a)"></div><h4>Lucy Ann Penfold</h4><p>Marketing Consultant</p></div>

<footer class="abs footer">
  <div class="brand"><span class="brand-dot"></span>Kindro</div>
  <p class="f-about">Lorem ipsum dolor sit amet, consec-tetur adipiscing elit, sed do eiusmod tempor incididunt ut labore et dolore magna aliqua. Quis ipsum sus-</p>
  <p class="f-copy">©2019 kindro.example. All rights reserved.</p>
  <ul class="f-nav"><li>HOME</li><li>ABOUT US</li><li>OUR SOLUTION</li><li>DEMONSTRATION</li><li>TESTIMONIALS</li><li>CONTACT US</li></ul>
  <div class="f-contact">
    <h5><svg width="10" height="10" aria-hidden="true"><path d="M2 0h3l1 3-2 1q1 2 3 3l1-2 3 1v3q-6 0-9-9Z" fill="#fff"/></svg>CALL US TODAY :-</h5>
    <p>Phone &nbsp;9000 4127.</p>
    <h5 style="margin-top:26px"><svg width="12" height="9" aria-hidden="true"><rect x=".5" y=".5" width="11" height="8" fill="none" stroke="#fff"/><path d="M.5 .5L6 5L11.5 .5" fill="none" stroke="#fff"/></svg>EMAIL :-</h5>
    <p>hello@kindro.example | Website : www.kindro.example</p>
  </div>
  <div class="f-social">STAY WITH US<div class="row"><span></span><span></span><span></span><span></span></div></div>
</footer>

</body>
</html>
```